Business Card Design Project - IT Company

CLOUD IT company working with medium to large corporate clients requires 2 sided Business Card design.

Strong, Professional and modern is what I am looking for.

The Logo JPG attached has all the colour palette options. which consist of Red and Silver on various backgrounds

Preferred option for the Back of card is either Silver Text on Red or Silver Text on Black. Though this is not concrete. Surprise me.

Logo must be prominent along with Contact details of the staff member

Tagline can be all Capitals " CLOUD MANAGED SERVICES"

I will look to provide feedback and tweaks to get the right design so it should be a fun process.

I will provide the layered files to the top few contenders.

Reason: Leaving the door open for some creativity. Don't forget this is an technology company. .

Target Market(s)

Leaders, decision makers, CEOs, CIOs,

Industry/Entity Type

Business

Requirements
Must have
• Data must have is

Company Name: Velquora
Tagline: Cloud Managed Services

No Particular order

First Name Last name
Director
Mobile 0452 987 654
www.velquora.com
First.Lastname@velquora.com
Suite 5, 48 Marlowe Lane, Sydney NSW 2000

```html
<!DOCTYPE html>
<html lang="en">
<head>
<meta charset="utf-8">
<title>Velquora Business Cards</title>
<link href="https://fonts.googleapis.com/css2?family=Rajdhani:wght@400;500;600;700&display=swap" rel="stylesheet">
<style>
  :root {
    --stage: #6e4528;
    --black: #050505;
    --red: #a31f25;
    --white: #ffffff;
    --silver: #d2d2d2;
    --silver-dim: #9a9a9a;
    --ink: #2a2a2a;
    --rule-dark: #5a5a5a;
    --rule-light: #c9c9c9;
  }
  * { box-sizing: border-box; margin: 0; padding: 0; }
  html, body { width: 1200px; height: 750px; overflow: hidden; }
  body {
    background: var(--stage);
    font-family: "Rajdhani", sans-serif;
    position: relative;
  }
  .card {
    position: absolute;
    width: 504px;
    height: 287px;
    overflow: hidden;
  }
  .card--front-black { left: 70px; top: 62px; background: var(--black); }
  .card--back-black { left: 625px; top: 62px; background: var(--black); }
  .card--front-red { left: 70px; top: 400px; background: var(--red); }
  .card--back-white { left: 625px; top: 400px; background: var(--white); }

  /* front */
  .front-logo {
    position: absolute;
    left: 0; right: 0; top: 88px;
    display: flex; flex-direction: column; align-items: center;
  }
  .front-logo__row { display: flex; align-items: center; gap: 16px; }
  .front-logo__dot {
    width: 62px; height: 62px; border-radius: 50%;
    background: var(--silver);
  }
  .front-logo__name {
    font-weight: 700; font-size: 80px; line-height: 0.9;
    color: var(--silver); letter-spacing: 1px;
  }
  .front-logo__tagline {
    align-self: flex-end; margin-right: 60px; margin-top: 2px;
    font-weight: 700; font-size: 15px; color: var(--silver); letter-spacing: 0.5px;
  }
  .front-rule {
    position: absolute; left: 95px; right: 95px; top: 242px; height: 2px;
    background: linear-gradient(90deg, transparent, var(--silver-dim), transparent);
  }
  .front-url {
    position: absolute; left: 0; right: 0; top: 251px;
    text-align: center; font-size: 18px; color: var(--white); letter-spacing: 2.5px;
  }
  .front-url b { font-weight: 700; }

  /* back */
  .back-logo {
    position: absolute; left: 22px; top: 40px;
    display: flex; flex-direction: column;
  }
  .back-logo__row { display: flex; align-items: center; gap: 7px; }
  .back-logo__dot { width: 28px; height: 28px; border-radius: 50%; }
  .back-logo__name { font-weight: 700; font-size: 40px; line-height: 0.9; }
  .back-logo__tagline {
    align-self: flex-end; font-weight: 700; font-size: 7.5px; letter-spacing: 0.3px;
  }
  .card--back-black .back-logo__dot { background: var(--silver); }
  .card--back-black .back-logo__name,
  .card--back-black .back-logo__tagline { color: var(--silver); }
  .card--back-white .back-logo__dot { background: var(--red); }
  .card--back-white .back-logo__name,
  .card--back-white .back-logo__tagline { color: var(--ink); }

  .person {
    position: absolute; right: 24px; top: 40px; text-align: right;
  }
  .person__name { font-weight: 700; font-size: 27px; line-height: 1; }
  .person__title { font-style: italic; font-size: 13px; margin-top: 6px; font-weight: 500; }
  .card--back-black .person__name, .card--back-black .person__title { color: var(--white); }
  .card--back-white .person__name { color: var(--red); }
  .card--back-white .person__title { color: var(--ink); }

  .rule {
    position: absolute; left: 282px; right: 22px; height: 1px;
  }
  .rule--top { top: 98px; }
  .rule--mid { top: 180px; }
  .card--back-black .rule { background: var(--rule-dark); }
  .card--back-white .rule { background: var(--rule-light); }

  .contact {
    position: absolute; right: 24px; list-style: none; text-align: right;
    font-size: 14px; font-weight: 500;
  }
  .contact--lines { top: 109px; }
  .contact--address { top: 190px; }
  .contact li { height: 20.5px; line-height: 20.5px; display: flex; justify-content: flex-end; align-items: center; }
  .contact li .icon { width: 11px; margin-left: 6px; display: inline-flex; justify-content: center; }
  .contact li .icon--none { width: 11px; margin-left: 6px; }
  .card--back-black .contact { color: var(--white); }
  .card--back-white .contact { color: var(--ink); }
  .card--back-black .icon svg { fill: var(--silver); }
  .card--back-white .icon svg { fill: var(--red); }
</style>
</head>
<body>

  <section class="card card--front-black">
    <div class="front-logo">
      <div class="front-logo__row">
        <span class="front-logo__dot"></span>
        <span class="front-logo__name">Velquora</span>
      </div>
      <span class="front-logo__tagline">CLOUD MANAGED SERVICES</span>
    </div>
    <div class="front-rule"></div>
    <p class="front-url">www.<b>velquora</b>.com</p>
  </section>

  <section class="card card--back-black">
    <div class="back-logo">
      <div class="back-logo__row">
        <span class="back-logo__dot"></span>
        <span class="back-logo__name">Velquora</span>
      </div>
      <span class="back-logo__tagline">CLOUD MANAGED SERVICES</span>
    </div>
    <div class="person">
      <p class="person__name">Daniel Morrow</p>
      <p class="person__title">Director</p>
    </div>
    <div class="rule rule--top"></div>
    <ul class="contact contact--lines">
      <li>0452 987 654<span class="icon"><svg width="6" height="10" viewBox="0 0 6 10"><rect x="0" y="0" width="6" height="10" rx="1"/></svg></span></li>
      <li>daniel.morrow@velquora.com<span class="icon"><svg width="10" height="7" viewBox="0 0 10 7"><rect width="10" height="7" rx="1"/></svg></span></li>
      <li>www.velquora.com<span class="icon"><svg width="9" height="9" viewBox="0 0 9 9"><circle cx="4.5" cy="4.5" r="4.5"/></svg></span></li>
    </ul>
    <div class="rule rule--mid"></div>
    <ul class="contact contact--address">
      <li>Suite 5, Level 5<span class="icon--none"></span></li>
      <li>48 Marlowe Lane<span class="icon"><svg width="10" height="15" viewBox="0 0 10 15"><path d="M5 0a5 5 0 0 0-5 5c0 4 5 10 5 10s5-6 5-10a5 5 0 0 0-5-5zm0 7a2 2 0 1 1 0-4 2 2 0 0 1 0 4z"/></svg></span></li>
      <li>SYDNEY NSW 2000<span class="icon--none"></span></li>
    </ul>
  </section>

  <section class="card card--front-red">
    <div class="front-logo">
      <div class="front-logo__row">
        <span class="front-logo__dot"></span>
        <span class="front-logo__name">Velquora</span>
      </div>
      <span class="front-logo__tagline">CLOUD MANAGED SERVICES</span>
    </div>
    <div class="front-rule"></div>
    <p class="front-url">www.<b>velquora</b>.com</p>
  </section>

  <section class="card card--back-white">
    <div class="back-logo">
      <div class="back-logo__row">
        <span class="back-logo__dot"></span>
        <span class="back-logo__name">Velquora</span>
      </div>
      <span class="back-logo__tagline">CLOUD MANAGED SERVICES</span>
    </div>
    <div class="person">
      <p class="person__name">Daniel Morrow</p>
      <p class="person__title">Director</p>
    </div>
    <div class="rule rule--top"></div>
    <ul class="contact contact--lines">
      <li>0452 987 654<span class="icon"><svg width="6" height="10" viewBox="0 0 6 10"><rect x="0" y="0" width="6" height="10" rx="1"/></svg></span></li>
      <li>daniel.morrow@velquora.com<span class="icon"><svg width="10" height="7" viewBox="0 0 10 7"><rect width="10" height="7" rx="1"/></svg></span></li>
      <li>www.velquora.com<span class="icon"><svg width="9" height="9" viewBox="0 0 9 9"><circle cx="4.5" cy="4.5" r="4.5"/></svg></span></li>
    </ul>
    <div class="rule rule--mid"></div>
    <ul class="contact contact--address">
      <li>Suite 5, Level 5<span class="icon--none"></span></li>
      <li>48 Marlowe Lane<span class="icon"><svg width="10" height="15" viewBox="0 0 10 15"><path d="M5 0a5 5 0 0 0-5 5c0 4 5 10 5 10s5-6 5-10a5 5 0 0 0-5-5zm0 7a2 2 0 1 1 0-4 2 2 0 0 1 0 4z"/></svg></span></li>
      <li>SYDNEY NSW 2000<span class="icon--none"></span></li>
    </ul>
  </section>

</body>
</html>
```